Packaging design for Virgin Coconut Oil. 100% pure cold pressed coconut oil

We need a new packaging and label design for our Virgin Coconut Oil product. It is currently marketed in the Philippines as a food supplement. We would like to try marketing it to other Asian countries such as Singapore, Malaysia and Hong Kong. The company has been producing this product since 2004 but now would like to venture into exporting our products overseas.

Would like to see designs with earth, natural "organic" colors. Fresh, Clean and pure look. Our trade mark is "Kestrel Meadow". Its a 100% pure cold pressed virgin coconut oil. All in all, we want to totally repackage our product and re-design the trademark to cater to export markets. Thanks!

Mid to High

Health Product

cadf82
9bcb3b
33b8a4
ffffff
3176b5
3276b5
0592cd
fbed22
fece3e

• Bottle shape design ideas.

```html
<!DOCTYPE html>
<html lang="en">
<head>
<meta charset="utf-8">
<title>Kestrel Meadow Coconut Oil Label</title>
<link rel="stylesheet" href="https://fonts.googleapis.com/css2?family=Montserrat:wght@400;500&family=Roboto:wght@400;700&family=Roboto+Condensed:wght@700&display=swap">
<style>
  :root {
    --page: #f4f2ef;
    --label-brown: #3e2c23;
    --label-brown-light: #4a362b;
    --leaf-tone: #5a4232;
    --accent-orange: #d8661d;
    --cream: #f3ece4;
    --cream-soft: #d9cfc4;
    --sketch: #8a7464;
  }
  * { margin: 0; padding: 0; box-sizing: border-box; }
  html, body {
    width: 1200px;
    height: 1200px;
    overflow: hidden;
    background: var(--page);
  }
  .canvas {
    position: relative;
    width: 1200px;
    height: 1200px;
  }
  .label {
    position: absolute;
    left: 100px;
    top: 320px;
    width: 1000px;
    height: 560px;
    background: radial-gradient(ellipse at 65% 45%, var(--label-brown-light), var(--label-brown) 70%);
    overflow: hidden;
    color: var(--cream);
  }
  .info-column {
    position: absolute;
    left: 40px;
    top: 30px;
    width: 300px;
    font-family: 'Roboto', sans-serif;
    font-size: 17px;
    line-height: 1.45;
    color: var(--cream-soft);
  }
  .info-column p { margin-bottom: 26px; }
  .palm-leaf-art {
    position: absolute;
    left: 560px;
    top: 90px;
    width: 300px;
    height: 220px;
    border-radius: 50% 50% 40% 40%;
    background: radial-gradient(ellipse at center, var(--leaf-tone), rgba(90,66,50,0) 70%);
    opacity: 0.8;
  }
  .coconut-art {
    position: absolute;
    left: 440px;
    top: 330px;
    width: 190px;
    height: 150px;
    border-radius: 50%;
    background: radial-gradient(ellipse at center, var(--sketch), rgba(138,116,100,0.15) 70%);
    opacity: 0.6;
  }
  .brand-name {
    position: absolute;
    left: 660px;
    top: 50px;
    font-family: 'Montserrat', sans-serif;
    font-weight: 400;
    font-size: 28px;
    letter-spacing: 1.5px;
    text-transform: uppercase;
    color: var(--cream);
  }
  .purity-badge {
    position: absolute;
    right: 130px;
    top: 220px;
    padding: 3px 10px;
    border: 2px solid var(--accent-orange);
    font-family: 'Roboto', sans-serif;
    font-weight: 700;
    font-size: 22px;
    color: var(--cream);
  }
  .product-type {
    position: absolute;
    right: 130px;
    top: 262px;
    font-family: 'Roboto', sans-serif;
    font-weight: 700;
    font-size: 27px;
    color: var(--cream);
  }
  .product-name {
    position: absolute;
    right: 126px;
    top: 292px;
    font-family: 'Roboto Condensed', sans-serif;
    font-weight: 700;
    font-size: 66px;
    letter-spacing: 1px;
    color: var(--accent-orange);
  }
  .accent-rule {
    position: absolute;
    left: 640px;
    top: 383px;
    width: 230px;
    height: 2px;
    background: var(--accent-orange);
  }
  .claims {
    position: absolute;
    left: 630px;
    top: 395px;
    font-family: 'Roboto', sans-serif;
    font-size: 20px;
    line-height: 1.05;
    color: var(--cream);
  }
  .claims .supplement { padding-left: 14px; letter-spacing: 1px; }
  .claims .natural { padding-left: 130px; }
  .net-weight {
    position: absolute;
    left: 790px;
    top: 505px;
    font-family: 'Roboto', sans-serif;
    font-size: 20px;
    color: var(--cream);
  }
</style>
</head>
<body>
<div class="canvas">
  <section class="label">
    <div class="info-column">
      <p>Made from fresh coconut meat, pressed cold to keep its gentle taste.</p>
      <p>Use one spoon daily, on its own or stirred into warm food.</p>
      <p>Store in a cool dry place. Solid below 24°C, clear when warm.</p>
      <p>Produced and packed in the Philippines for export markets.</p>
    </div>

    <div class="palm-leaf-art" role="img" aria-label="Faint palm leaf illustration"></div>
    <div class="coconut-art" role="img" aria-label="Sketch of a halved coconut with palm leaves"></div>

    <div class="brand-name">Kestrel Meadow</div>
    <div class="purity-badge">100% PURE</div>
    <div class="product-type">COLD PRESSED VIRGIN</div>
    <div class="product-name">COCONUT OIL</div>
    <div class="accent-rule"></div>
    <div class="claims">
      <div class="claim">Approved therapeutic claim</div>
      <div class="supplement">FOOD SUPPLEMENT</div>
      <div class="natural">All Natural</div>
    </div>
    <div class="net-weight">Net .Wt .50 oz</div>
  </section>
</div>
</body>
</html>
```